Business card design needed

We would like a new design for our window furnishings & home decor business. We supply & install blinds, curtains, shutters etc. We are about to incorporate home decor products like cushoins & throws...
We'd like to use moderns browns & green tones. Casual but elegant style. Maybe textured/patterned look design. Design should communicate quality and great value with latest designs.

website & FB page & email is still to be advised so pls provide space.

Contact Information for Business Card

Marlow Haven
Window Furnishings & Home Decor
Gabrielle - Interior Stylist
Call us now for a free measure & quote - 63124098
0412 905 316
0418 276 540

```html
<!DOCTYPE html>
<html lang="en">
<head>
<meta charset="utf-8">
<title>Marlow Haven – Business Card</title>
<link rel="stylesheet" href="https://fonts.googleapis.com/css2?family=Questrial&display=swap">
<style>
  :root {
    --leaf: #a9c43f;
    --leaf-band: #adb83c;
    --leaf-text: #b8c640;
    --earth: #3f2814;
    --earth-text: #4a2e14;
    --icon: #dcdcc8;
    --paper: #ffffff;
  }
  * { margin: 0; padding: 0; box-sizing: border-box; }
  html, body {
    width: 1027px;
    height: 1200px;
    overflow: hidden;
    background: var(--paper);
    font-family: "Questrial", "Century Gothic", sans-serif;
  }
  .canvas { position: relative; width: 1027px; height: 1200px; }

  .card-front {
    position: absolute; left: 0; top: 0; width: 1027px; height: 581px;
    overflow: hidden;
  }
  .card-front .wood {
    position: absolute; inset: 0; width: 100%; height: 100%;
  }
  .brand-name {
    position: absolute; left: 0; width: 100%; top: 210px;
    text-align: center; font-size: 78px; font-weight: 400; line-height: 1;
    color: var(--leaf); letter-spacing: 0.5px;
  }
  .brand-tagline {
    position: absolute; left: 0; width: 100%; top: 299px;
    text-align: center; font-size: 35px; line-height: 1;
    color: var(--paper);
  }
  .brand-tagline .small { font-size: 29px; }

  .card-back {
    position: absolute; left: 0; top: 598px; width: 1027px; height: 602px;
  }
  .band-name {
    position: absolute; left: 0; top: 0; width: 100%; height: 322px;
    background: var(--leaf-band);
  }
  .person-name {
    position: absolute; left: 0; width: 100%; top: 164px;
    text-align: center; font-size: 60px; font-weight: 400; line-height: 1;
    color: var(--earth-text);
  }
  .person-role {
    position: absolute; left: 0; width: 100%; top: 229px;
    text-align: center; font-size: 27px; line-height: 1;
    color: var(--earth-text);
  }
  .band-contact {
    position: absolute; left: 0; top: 322px; width: 100%; height: 280px;
    background: var(--earth);
  }
  .call-to-action {
    position: absolute; left: 0; width: 100%; top: 27px;
    text-align: center; font-size: 35px; line-height: 1;
    color: var(--paper);
  }
  .divider {
    position: absolute; left: 558px; top: 86px; width: 3px; height: 154px;
    background: var(--leaf-text);
  }
  .contact-text {
    position: absolute; font-size: 29px; line-height: 1; color: var(--leaf-text);
    white-space: nowrap;
  }
  .email-label { right: 544px; top: 104px; }
  .email-icon { position: absolute; left: 502px; top: 106px; }
  .website { right: 489px; top: 188px; }
  .phone-icon { position: absolute; left: 578px; }
  .phone-list .contact-text { left: 620px; }
</style>
</head>
<body>
<div class="canvas">

  <section class="card-front">
    <svg class="wood" viewBox="0 0 1027 581" preserveAspectRatio="none" role="img" aria-label="Dark stained wood plank texture">
      <defs>
        <radialGradient id="woodGlow" cx="50%" cy="52%" r="60%">
          <stop offset="0" stop-color="#8a4d2d"/>
          <stop offset="0.35" stop-color="#5a2f18"/>
          <stop offset="1" stop-color="#1a0c05"/>
        </radialGradient>
      </defs>
      <rect width="1027" height="581" fill="url(#woodGlow)"/>
    </svg>
    <h1 class="brand-name">Marlow Haven</h1>
    <p class="brand-tagline">Window Furnishings <span class="small">&amp; Home Decor</span></p>
  </section>

  <section class="card-back">
    <div class="band-name">
      <h2 class="person-name">Gabrielle</h2>
      <p class="person-role">Interior Stylist</p>
    </div>
    <div class="band-contact">
      <p class="call-to-action">Call us now for a free measure &amp; quote</p>

      <span class="contact-text email-label">Email</span>
      <svg class="email-icon" width="30" height="22" viewBox="0 0 30 22" aria-hidden="true">
        <rect x="1.5" y="1.5" width="27" height="19" fill="none" stroke="var(--icon)" stroke-width="2.5"/>
        <path d="M2 2 L15 13 L28 2 M2 20 L11 10 M28 20 L19 10" fill="none" stroke="var(--icon)" stroke-width="2.5"/>
      </svg>

      <span class="contact-text website">www.marlowhaven.com</span>

      <div class="divider"></div>

      <svg class="phone-icon" style="top:108px" width="22" height="26" viewBox="0 0 22 26" aria-hidden="true">
        <path d="M8 2 C3 4 2 10 5 16 C8 22 13 25 18 24 L20 19 L15 16 L12 18 C9 16 7 12 7 9 L10 7 L9 1 Z" fill="var(--icon)"/>
      </svg>
      <svg class="phone-icon" style="top:145px" width="22" height="28" viewBox="0 0 22 28" aria-hidden="true">
        <rect x="2" y="1" width="18" height="26" rx="2" fill="var(--icon)"/>
        <rect x="5" y="4" width="12" height="8" fill="var(--earth)"/>
        <g fill="var(--earth)">
          <rect x="5" y="15" width="3" height="2"/><rect x="10" y="15" width="3" height="2"/><rect x="15" y="15" width="2" height="2"/>
          <rect x="5" y="19" width="3" height="2"/><rect x="10" y="19" width="3" height="2"/><rect x="15" y="19" width="2" height="2"/>
          <rect x="5" y="23" width="3" height="2"/><rect x="10" y="23" width="3" height="2"/><rect x="15" y="23" width="2" height="2"/>
        </g>
      </svg>

      <div class="phone-list">
        <span class="contact-text" style="top:109px">63124098</span>
        <span class="contact-text" style="top:148px">0412 905 316</span>
        <span class="contact-text" style="top:187px">0418 276 540</span>
      </div>
    </div>
  </section>

</div>
</body>
</html>
```